PLM - Business Card Design Project

We need a business card based on our logo
Updates

Hi I just upload logo file in AI format Thanks and regards

Target Market(s)

Bank, Big companies, Business owners

Industry/Entity Type

Business

Font styles to use
Sans Serif

```html
<!DOCTYPE html>
<html lang="fr">
<head>
<meta charset="utf-8">
<title>PLM – Carte de visite</title>
<link rel="stylesheet" href="https://fonts.googleapis.com/css2?family=Poppins:wght@300;400;500;600&display=swap">
<style>
  :root {
    --page-bg: #2b2d31;
    --card-white: #ffffff;
    --navy: #1d3a66;
    --navy-deep: #17325a;
    --navy-light: #2a4f80;
    --ink-grey: #5e6266;
    --text-light: #ffffff;
  }
  * { box-sizing: border-box; margin: 0; padding: 0; }
  html, body {
    width: 1200px;
    height: 784px;
    overflow: hidden;
    background: var(--page-bg);
    font-family: "Poppins", sans-serif;
  }
  .canvas {
    position: relative;
    width: 1200px;
    height: 784px;
  }
  .business-card {
    position: absolute;
    left: 150px;
    top: 135px;
    width: 900px;
    height: 514px;
    background: var(--card-white);
    overflow: hidden;
    box-shadow: 0 18px 40px rgba(0,0,0,0.45);
  }
  .card-band {
    position: absolute;
    left: 0;
    right: 0;
    bottom: 0;
    height: 278px;
    background: linear-gradient(160deg, var(--navy-light) 0%, var(--navy) 45%, var(--navy-deep) 100%);
  }
  .brand {
    position: absolute;
    left: 56px;
    top: 64px;
    color: var(--navy);
  }
  .brand-mark {
    display: flex;
    align-items: center;
    gap: 16px;
  }
  .brand-initials {
    font-weight: 300;
    font-size: 104px;
    line-height: 0.9;
    letter-spacing: 2px;
    color: var(--navy);
  }
  .brand-dot {
    width: 22px;
    height: 22px;
    border-radius: 50%;
    background: var(--navy);
    margin-top: 30px;
  }
  .brand-name {
    margin-top: 10px;
    font-weight: 300;
    font-size: 27px;
    color: var(--navy);
    letter-spacing: 0.3px;
  }
  .brand-tagline {
    margin-top: 2px;
    font-weight: 300;
    font-size: 13px;
    color: var(--ink-grey);
    letter-spacing: 0.6px;
  }
  .holder {
    position: absolute;
    right: 48px;
    top: 44px;
    text-align: right;
    color: var(--ink-grey);
  }
  .holder-name {
    font-weight: 600;
    font-size: 34px;
    line-height: 1.15;
  }
  .holder-role {
    font-weight: 500;
    font-size: 30px;
    line-height: 1.2;
  }
  .contact-list {
    position: absolute;
    left: 60px;
    bottom: 48px;
    list-style: none;
    color: var(--text-light);
  }
  .contact-item {
    display: flex;
    align-items: center;
    gap: 12px;
    font-weight: 400;
    font-size: 30px;
    line-height: 1.5;
  }
  .contact-icon {
    width: 26px;
    height: 26px;
    flex: none;
  }
</style>
</head>
<body>
<main class="canvas">
  <section class="business-card">
    <div class="card-band"></div>

    <div class="brand">
      <div class="brand-mark">
        <span class="brand-initials">PLM</span>
        <span class="brand-dot"></span>
      </div>
      <p class="brand-name">Cabinet Perrin Lemaire &amp; Associés</p>
      <p class="brand-tagline">Expertise-comptable · Audit · Conseil</p>
    </div>

    <div class="holder">
      <p class="holder-name">Name</p>
      <p class="holder-role">Designation</p>
    </div>

    <ul class="contact-list">
      <li class="contact-item">
        <svg class="contact-icon" viewBox="0 0 24 24" aria-hidden="true">
          <path fill="#fff" d="M6.6 10.8a15.1 15.1 0 0 0 6.6 6.6l2.2-2.2a1 1 0 0 1 1-.25 11.4 11.4 0 0 0 3.6.57 1 1 0 0 1 1 1V20a1 1 0 0 1-1 1A17 17 0 0 1 3 4a1 1 0 0 1 1-1h3.5a1 1 0 0 1 1 1c0 1.25.2 2.45.57 3.57a1 1 0 0 1-.25 1z"/>
        </svg>
        <span>Ph</span>
      </li>
      <li class="contact-item">
        <svg class="contact-icon" viewBox="0 0 24 24" aria-hidden="true">
          <path fill="#fff" d="M2 6h20v12H2z"/>
          <path fill="none" stroke="#1d3a66" stroke-width="1.6" d="M2 6l10 7 10-7"/>
        </svg>
        <span>Email</span>
      </li>
      <li class="contact-item">
        <svg class="contact-icon" viewBox="0 0 24 24" aria-hidden="true">
          <circle cx="12" cy="12" r="10" fill="#fff"/>
          <g fill="none" stroke="#1d3a66" stroke-width="1.3">
            <ellipse cx="12" cy="12" rx="4.5" ry="10"/>
            <path d="M2 12h20M4 7h16M4 17h16M12 2v20"/>
          </g>
        </svg>
        <span>Web</span>
      </li>
    </ul>
  </section>
</main>
</body>
</html>
```